Website Design for a High School

School Name: Bayt Nakhla Private Schools
sub-schools:
1-Bayt Nakhla Primary School
2-Bayt Nakhla High School for Girls
3-Bayt Nakhla High School for Boys
The design should be professional and serious and below is the details of the website.
Pages: (Home, About Us, Schools, Events, Students, Gallery, Lectures, Contact Us).
A-) Home Page:
1-Animated photos banner as main
2-Marquee for the last news.
3-Welcoming block of text
4-latest news at the body of the page.
5-Calender "on the side"
6-Number of visitors "on the side"
7-Search bar
8-options to choose a school
B-) School Page:
three schools listed as drop down menu when highlighted over the Schools button in the menu
*Each school page should contain:
1-Student login area
2-Animation photos header
3-Specific news and projects
C-) Student Login page:
have a Report Card
D-) Gallery Page
have a collection of photos.
E-)Contact Page
phone numbers
emails
feedback form
F-)Other mentioned pages
with normal text and photos page look as similar to the Home page.
Required color: Purple as main and include the logo colors
Logo: is attached.
Button link to change language to Arabic.
School
5+ page

```html
<!DOCTYPE html>
<html lang="en">
<head>
<meta charset="utf-8">
<title>Bayt Nakhla Private Schools</title>
<link rel="stylesheet" href="https://fonts.googleapis.com/css2?family=Source+Sans+3:ital,wght@0,400;0,600;0,700;1,400;1,600;1,700&display=swap">
<style>
:root{
  --teal:#2bb3ad;
  --teal-light:#8fdcd6;
  --sky:#6fd3f2;
  --purple:#7b3c9e;
  --purple-dark:#5d2a82;
  --orange:#f39a1e;
  --yellow:#fde08a;
  --gold:#f2c94c;
  --grey-band:#5b5b5b;
  --footer:#2f2f2f;
  --ink:#222;
  --link:#2a7fc1;
  --cal:#e9c98f;
  --cal-cell:#f3d9a4;
}
*{box-sizing:border-box;margin:0;padding:0}
html,body{width:1200px;height:3109px;overflow:hidden}
body{position:relative;font-family:"Source Sans 3",Arial,sans-serif;color:var(--ink);background:#fff}
.abs{position:absolute}

/* header */
.header{left:0;top:0;width:1200px;height:742px;background:linear-gradient(180deg,var(--teal) 0%,#5cc6bf 35%,#b9dcd9 75%,#dcdcdc 100%)}
.brand{left:83px;top:10px;width:166px;height:177px;border-radius:50%;background:#fff;border:6px solid var(--purple-dark);display:flex;align-items:center;justify-content:center;text-align:center;font-weight:700;font-size:24px;color:var(--purple-dark)}
.nav{left:421px;top:30px;display:flex;gap:30px;font-weight:700;font-size:17px;color:var(--yellow);text-transform:uppercase;letter-spacing:-.3px}
.nav span.drop::after{content:"";display:inline-block;margin-left:5px;border:5px solid transparent;border-top:6px solid var(--yellow);vertical-align:-2px}
.site-title{left:0;width:1200px;top:115px;text-align:center;font-size:42px;font-weight:700;color:var(--purple)}
.slide{left:81px;top:199px;width:1040px;height:489px;background:linear-gradient(180deg,#3b5e78 0%,#7fa0a6 45%,#8a8a6e 80%,#6d7a4b 100%)}
.slide-caption{left:614px;top:240px;color:#fff}
.slide-caption h2{font-size:32px;font-weight:700;color:var(--gold);margin-bottom:6px}
.slide-caption li{list-style:none;font-size:21px;font-weight:700;font-style:italic;line-height:28px;display:flex;align-items:center;gap:12px}
.arrow{top:385px;width:40px;height:90px}

/* news ticker */
.ticker{left:81px;top:781px;width:1040px;height:79px;background:var(--yellow);display:flex;align-items:center;padding-left:4px;gap:0;overflow:hidden;white-space:nowrap}
.ticker b{color:var(--teal);font-size:22px;margin-right:30px}
.ticker span{font-size:16px;font-style:italic;color:var(--purple);margin-right:40px;display:flex;align-items:center;gap:8px}
.ticker span::before{content:"";width:10px;height:10px;border-radius:50%;border:1.5px solid var(--purple)}

/* welcome */
.welcome{left:0;top:896px;width:1200px;height:393px;background:linear-gradient(90deg,#66cbea,#8fdcf5 50%,#6fd3f2)}
.welcome-text{left:97px;top:926px;width:1040px;color:var(--purple);font-style:italic;font-weight:700;font-size:22.5px;line-height:37px}
.welcome-text p+p{margin-top:32px}

/* news */
.section-title{font-size:27px;font-weight:700;color:var(--orange)}
.news-title{left:81px;top:1313px}
.rule{height:2px;background:var(--purple)}
.news-item{top:1376px;width:340px}
.news-logo{width:92px;height:92px;border-radius:50%;border:4px solid var(--purple-dark);background:#fff;margin-left:50px;display:flex;align-items:center;justify-content:center;font-size:13px;font-weight:700;color:var(--purple-dark)}
.news-item h3{margin-top:22px;font-size:19px;font-style:italic;font-weight:700;color:var(--purple)}
.news-meta{font-size:12px;font-style:italic;display:flex;gap:38px;margin-top:2px}
.news-meta i{font-style:normal;font-weight:700;display:flex;align-items:center;gap:4px}
.news-meta i::before{content:"";width:14px;height:12px;border-radius:50%;background:var(--orange)}
.news-item p{font-size:12.5px;line-height:12.5px;margin-top:6px}
.more{display:block;text-align:right;font-size:12px;color:var(--link);margin-top:10px;font-style:italic}
.dots{display:flex;gap:14px}
.dots i{width:14px;height:14px;border-radius:50%;background:#cfcfcf}
.dots i.on{background:#2346a8}
.find{font-weight:700;font-size:20px;color:var(--purple-dark);display:flex;align-items:center;gap:8px}
.social{width:32px;height:32px;border-radius:50%;background:var(--purple)}
.calendar{left:810px;top:1372px;width:311px;height:278px;background:var(--cal)}
.cal-head{height:36px;display:flex;align-items:center;justify-content:center;font-weight:700;font-size:16px;position:relative}
.cal-head .nb{position:absolute;top:8px;width:20px;height:20px;border-radius:50%;background:#fff}
.cal-days,.cal-row{display:grid;grid-template-columns:repeat(7,1fr)}
.cal-days{font-size:10px;text-align:center;height:30px;line-height:30px;color:#555}
.cal-row{gap:2px;padding:0 2px;margin-bottom:2px}
.cal-row span{height:38px;background:var(--cal-cell);display:flex;align-items:center;justify-content:center;font-size:16px}
.cal-row span.off{color:#b89b6a;background:#f0dcb5}
.cal-row span.today{background:#111;color:#fff}

/* schools */
.schools{left:0;top:1679px;width:1200px;height:425px;background:linear-gradient(180deg,#9fe6e0,#dff4f2)}
.schools-title{left:0;width:1200px;top:1696px;text-align:center;font-size:27px;font-weight:700;color:var(--purple-dark)}
.school-card{top:1756px;width:302px}
.school-photo{height:197px;position:relative}
.school-photo b{position:absolute;left:0;right:0;bottom:0;height:25px;background:rgba(90,90,90,.55);color:var(--orange);font-style:italic;font-size:16px;text-align:center;line-height:25px}
.school-card p{font-size:12.5px;line-height:15.5px;margin-top:20px}
.school-card .more{margin-top:10px}

/* contact */
.quick{left:81px;top:2131px;width:759px;height:249px;background:var(--yellow)}
.quick h2{text-align:center;font-size:29px;color:var(--purple);margin-top:6px}
.quick .sub{text-align:center;font-size:15px;color:var(--purple);font-weight:600}
.field{background:#ececec;font-size:14px;color:#777;padding:8px 12px}
.submit{left:728px;top:2330px;width:97px;height:35px;background:#2b2b2b;color:#fff;font-weight:700;font-size:18px;border-radius:3px;display:flex;align-items:center;justify-content:center}
.counter{left:864px;top:2131px;width:257px;height:249px;background:var(--purple);border-radius:8px;padding:0 8px 8px}
.counter h2{color:#fff;text-align:center;font-size:25px;line-height:34px}
.counter-body{background:#fff;height:198px;padding:8px 14px 0 12px;font-size:17px}
.crow{display:flex;align-items:center;height:23px}
.crow i{width:14px;height:16px;border-radius:6px 6px 3px 3px;background:var(--orange);margin-right:12px}
.crow span{flex:1}
.online{border-top:2px solid #333;margin-top:10px;padding-top:4px;text-align:center}

/* guardians */
.guardians{left:0;top:2409px;width:1200px;height:361px;background:linear-gradient(180deg,#555,#6a6a6a)}
.guardians h2{left:81px;top:2426px;color:#fff;font-size:26px}
.avatar{width:108px;height:108px;border-radius:50%;background:linear-gradient(160deg,#d9d9d9,#9a9a9a);border:3px solid #fff}
.quote{color:#fff;font-style:italic;font-size:14px;line-height:22.5px}
.who{color:var(--orange);font-style:italic;font-weight:700;font-size:12.5px}

/* footer */
.footer{left:0;top:2770px;width:1200px;height:339px;background:var(--footer);color:#fff}
.copy{left:83px;top:2793px;font-size:15px;font-weight:600;color:#fff;display:flex;align-items:center;gap:10px}
.copy::before{content:"©";width:20px;height:20px;border:1.5px solid #fff;border-radius:50%;display:flex;align-items:center;justify-content:center;font-size:13px}
.foot-logo{left:83px;top:2834px;width:228px;height:228px;border-radius:50%;background:#fff;border:8px solid var(--purple-dark);display:flex;align-items:center;justify-content:center;font-size:30px;font-weight:700;color:var(--purple-dark)}
.foot-h{font-size:19px;font-weight:700;color:#fff}
.foot-rule{height:1.5px;background:#888}
.contact-row{left:547px;display:flex;align-items:center;gap:16px;font-size:15px;font-weight:700;color:#fff}
.contact-row svg{flex:none}
.links{left:984px;top:2832px;list-style:none;font-size:15px;font-weight:700;color:var(--teal-light);line-height:24.4px;text-transform:uppercase}
</style>
</head>
<body>

<header class="abs header"></header>
<div class="abs brand">Bayt<br>Nakhla</div>
<nav class="abs nav"><span>Home</span><span>About Us</span><span class="drop">Schools</span><span>Events</span><span>Students</span><span>Gallery</span><span>Lectures</span><span>Contact Us</span></nav>
<h1 class="abs site-title">Bayt Nakhla Private Schools</h1>

<div class="abs slide" role="img" aria-label="Photo of the modern glass-fronted school building"></div>
<div class="abs slide-caption">
  <h2>Lorem ipsum dolor sit amet</h2>
  <ul>
    <li><svg width="20" height="18" viewBox="0 0 20 18"><path d="M2 9l6 6L18 2" stroke="#fff" stroke-width="4" fill="none"/></svg>Lorem ipsum dolor sit amet, consectetor</li>
    <li><svg width="20" height="18" viewBox="0 0 20 18"><path d="M2 9l6 6L18 2" stroke="#fff" stroke-width="4" fill="none"/></svg>Lorem ipsum dolor sit amet, consectetor</li>
    <li><svg width="20" height="18" viewBox="0 0 20 18"><path d="M2 9l6 6L18 2" stroke="#fff" stroke-width="4" fill="none"/></svg>Lorem ipsum dolor sit amet, consectetor</li>
  </ul>
</div>
<svg class="abs arrow" style="left:22px" viewBox="0 0 40 90"><path d="M32 4L8 45l24 41" stroke="#fff" stroke-width="4" fill="none"/></svg>
<svg class="abs arrow" style="left:1138px" viewBox="0 0 40 90"><path d="M8 4l24 41L8 86" stroke="#fff" stroke-width="4" fill="none"/></svg>

<div class="abs ticker"><b>Last News :</b><span>Lorem ipsum dolor sit amet, consectetor</span><span>Lorem ipsum dolor sit amet, consectetor</span><span>Lorem ipsum dolor sit amet, consectetor</span></div>

<section class="abs welcome" role="img" aria-label="Faint background photo of students in a classroom"></section>
<div class="abs welcome-text">
  <p>Bayt Nakhla Private Schools is a school that … … … … … … … …<br>Lorem ipsum dolor sit amet, consectet dolor sit amet, Lorem ipsum dolor sit amet, consectet dolor sit<br>Lorem ipsum dolor sit amet, consectet dolor sit amet, Lorem ipsum dolor sit amet, consectet dolor sit<br>Lorem ipsum dolor sit amet, consectet dolor sit amet, Lorem ipsum dolor sit amet, consectet dolor sit</p>
  <p>Bayt Nakhla Private Schools is a school that … … … … … … … …<br>Lorem ipsum dolor sit amet, consectet dolor sit amet, Lorem ipsum dolor sit amet, consectet dolor sit<br>Lorem ipsum dolor sit amet, consectet dolor sit amet, Lorem ipsum dolor sit amet, consectet dolor sit<br>Lorem ipsum dolor sit amet, consectet dolor sit amet, Lorem ipsum dolor sit amet, consectet dolor sit</p>
</div>

<h2 class="abs section-title news-title">Latest News &amp; Events</h2>
<div class="abs rule" style="left:81px;top:1351px;width:674px"></div>
<article class="abs news-item" style="left:81px">
  <div class="news-logo">Bayt Nakhla</div>
  <h3>Lorem ipsum dolor sit amet</h3>
  <div class="news-meta"><span>May 10, 2015</span><i>05</i></div>
  <p>Lorem ipsum dolor sit amet consectet dolor<br>Lorem ipsum dolor sit amet consectet dolor<br>Lorem ipsum dolor sit amet consectet dolor<br>Lorem ipsum dolor sit amet consectet dolor</p>
  <span class="more">Continue … …</span>
</article>
<article class="abs news-item" style="left:458px">
  <div class="news-logo">Bayt Nakhla</div>
  <h3>Lorem ipsum dolor sit amet</h3>
  <div class="news-meta"><span>May 10, 2015</span><i>10</i></div>
  <p>Lorem ipsum dolor sit amet consectet dolor<br>Lorem ipsum dolor sit amet consectet dolor<br>Lorem ipsum dolor sit amet consectet dolor<br>Lorem ipsum dolor sit amet consectet dolor</p>
  <span class="more">Continue … …</span>
</article>
<div class="abs dots" style="left:366px;top:1633px"><i></i><i></i><i class="on"></i><i></i><i></i></div>

<div class="abs find" style="left:810px;top:1318px">Find us on:<i class="social"></i><i class="social"></i><i class="social"></i><i class="social"></i><i class="social"></i></div>
<div class="abs calendar">
  <div class="cal-head"><i class="nb" style="left:14px"></i>March 2015<i class="nb" style="right:14px"></i></div>
  <div class="cal-days"><span>MON</span><span>TUE</span><span>WED</span><span>THU</span><span>FRI</span><span>SAT</span><span>SUN</span></div>
  <div class="cal-row"><span class="off">28</span><span>1</span><span>2</span><span>3</span><span class="today">4</span><span>5</span><span>6</span></div>
  <div class="cal-row"><span>7</span><span>8</span><span>9</span><span>10</span><span>11</span><span>12</span><span>13</span></div>
  <div class="cal-row"><span>14</span><span>15</span><span>16</span><span>17</span><span>18</span><span>19</span><span>20</span></div>
  <div class="cal-row"><span>21</span><span>22</span><span>23</span><span>24</span><span>25</span><span>26</span><span>27</span></div>
  <div class="cal-row"><span>28</span><span>29</span><span>30</span><span>31</span><span class="off">1</span><span class="off">2</span><span class="off">3</span></div>
</div>

<section class="abs schools"></section>
<h2 class="abs schools-title">Choose Your School</h2>
<div class="abs rule" style="left:81px;top:1730px;width:1040px;background:#555;height:1.5px"></div>
<article class="abs school-card" style="left:81px">
  <div class="school-photo" role="img" aria-label="Photo of a group of primary pupils with backpacks" style="background:linear-gradient(180deg,#e8e8e8,#b7a98a)"><b>Bayt Nakhla Primary School</b></div>
  <p>Lorem ipsum dolor sit amet, consectetur adipiscing<br>Lorem ipsum dolor sit amet, consectetur adipiscing<br>Lorem ipsum dolor sit amet, consectetur adipiscing<br>Lorem ipsum dolor sit amet, consectetur adipiscing<br>Lorem ipsum dolor sit amet, consectetur adipiscing</p>
  <span class="more">View Details</span>
</article>
<article class="abs school-card" style="left:450px">
  <div class="school-photo" role="img" aria-label="Photo of a smiling girl student in front of a school" style="background:linear-gradient(180deg,#6e8fb8,#8a6d4e 60%,#3f6a3a)"><b>Bayt Nakhla High School for Girls</b></div>
  <p>Lorem ipsum dolor sit amet, consectetur adipiscing<br>Lorem ipsum dolor sit amet, consectetur adipiscing<br>Lorem ipsum dolor sit amet, consectetur adipiscing<br>Lorem ipsum dolor sit amet, consectetur adipiscing<br>Lorem ipsum dolor sit amet, consectetur adipiscing</p>
  <span class="more">View Details</span>
</article>
<article class="abs school-card" style="left:819px">
  <div class="school-photo" role="img" aria-label="Photo of a boy doing a science experiment" style="background:linear-gradient(180deg,#4f8a55,#a4c79a 60%,#d6d9c8)"><b>Bayt Nakhla High School for Boys</b></div>
  <p>Lorem ipsum dolor sit amet, consectetur adipiscing<br>Lorem ipsum dolor sit amet, consectetur adipiscing<br>Lorem ipsum dolor sit amet, consectetur adipiscing<br>Lorem ipsum dolor sit amet, consectetur adipiscing<br>Lorem ipsum dolor sit amet, consectetur adipiscing</p>
  <span class="more">View Details</span>
</article>

<section class="abs quick">
  <h2>Quick Contact</h2>
  <p class="sub">Lorem ipsum dolor sit amet, consectetur adipiscing elit.</p>
</section>
<div class="abs field" style="left:93px;top:2230px;width:232px;height:42px">Name</div>
<div class="abs field" style="left:342px;top:2230px;width:234px;height:42px">Email</div>
<div class="abs field" style="left:593px;top:2230px;width:234px;height:42px">Phone</div>
<div class="abs field" style="left:93px;top:2289px;width:483px;height:76px">Message</div>
<div class="abs submit">Submit</div>

<aside class="abs counter">
  <h2>Visit Counter</h2>
  <div class="counter-body">
    <div class="crow"><i></i><span>Today</span>11</div>
    <div class="crow"><i></i><span>Yesterday</span>33</div>
    <div class="crow"><i></i><span>This week</span>554</div>
    <div class="crow"><i></i><span>Last week</span>751</div>
    <div class="crow"><i></i><span>This month</span>1791</div>
    <div class="crow"><i></i><span>Last month</span>3674</div>
    <div class="crow"><i style="background:#7aa0d8"></i><span>All</span>12462</div>
    <div class="online">Online now: 2</div>
  </div>
</aside>

<section class="abs guardians"></section>
<h2 class="abs guardians" style="left:81px;top:2426px;width:auto;height:auto;background:none;color:#fff;font-size:26px">What Guardians Say</h2>
<div class="abs avatar" role="img" aria-label="Portrait photo of a parent" style="left:81px;top:2543px"></div>
<p class="abs quote" style="left:209px;top:2544px;width:360px">Lorem ipsum dolor sit amet, consectetur adipiscing elit.<br>Curabitur non bibendum leo. Ut blandit in leo sit amet .<br>Nibh tellus efficitur magna, at blandit nibh ligula eu mi.<br>Suspendisse fermentum, nisl eget accumsan posuere.<br>Suspendisse fermentum, nisl eget accumsan posuere.</p>
<span class="abs who" style="left:460px;top:2673px">Lidia, NA, NY</span>
<div class="abs avatar" role="img" aria-label="Portrait photo of a parent" style="left:645px;top:2543px"></div>
<p class="abs quote" style="left:773px;top:2544px;width:360px">Lorem ipsum dolor sit amet, consectetur adipiscing elit.<br>Curabitur non bibendum leo. Ut blandit in leo sit amet .<br>Nibh tellus efficitur magna, at blandit nibh ligula eu mi.<br>Suspendisse fermentum, nisl eget accumsan posuere.<br>Suspendisse fermentum, nisl eget accumsan posuere.</p>
<span class="abs who" style="left:992px;top:2673px">Tomas, Liverpool, NSW</span>
<div class="abs dots" style="left:570px;top:2731px"><i style="background:#ddd"></i><i style="background:#ddd"></i><i class="on"></i><i style="background:#ddd"></i><i style="background:#ddd"></i></div>

<footer class="abs footer"></footer>
<div class="abs copy">All Rights Reserved 2015</div>
<div class="abs foot-logo">Bayt Nakhla</div>

<h3 class="abs foot-h" style="left:547px;top:2788px">Contact Us</h3>
<div class="abs foot-rule" style="left:547px;top:2822px;width:296px"></div>
<div class="abs contact-row" style="top:2852px">
  <svg width="26" height="26" viewBox="0 0 26 26"><rect width="26" height="26" rx="3" fill="#9a9a9a"/><path d="M13 5a5 5 0 0 0-5 5c0 4 5 11 5 11s5-7 5-11a5 5 0 0 0-5-5z" fill="#fff"/><circle cx="13" cy="10" r="2" fill="#9a9a9a"/></svg>
  000 Aaaaaaaa,Bbbbbb, Ccccccc, Dd 10001, Eeee</div>
<div class="abs contact-row" style="top:2895px">
  <svg width="26" height="26" viewBox="0 0 26 26"><rect width="26" height="26" rx="3" fill="#9a9a9a"/><path d="M8 6l3 0 1 4-2 1.5a9 9 0 0 0 4.5 4.5L16 14l4 1v3c-7 1-13-5-12-12z" fill="#fff"/></svg>
  +00 000000000000</div>
<div class="abs contact-row" style="top:2931px">
  <svg width="26" height="20" viewBox="0 0 26 20"><rect x="1" y="1" width="24" height="18" fill="#ddd"/><path d="M1 1l12 10L25 1" stroke="#888" stroke-width="1.5" fill="none"/></svg>
  info@baytnakhla-schools.example</div>
<div class="abs find" style="left:553px;top:2981px;color:#fff">Find us on:<i class="social"></i><i class="social"></i><i class="social"></i><i class="social"></i><i class="social"></i></div>

<h3 class="abs foot-h" style="left:978px;top:2788px">Quick Links</h3>
<div class="abs foot-rule" style="left:978px;top:2822px;width:143px"></div>
<ul class="abs links">
  <li>Home</li><li>About Us</li><li>Schools</li><li>Events</li><li>Students</li><li>Gallery</li><li>Lectures</li><li>Contact Us</li><li>Privacy Policy</li><li>Join Us</li>
</ul>

</body>
</html>
```